Zielgruppe
Einzelnfirmen, Arbeitsgruppen und KMU im Dienstleistungssektor.
Aufgabenstellung
Vorweg: Dem Auftrag folgen weitere Teilaufträge an den Gewinner, natürlich gegen Bezahlung.
Für die bereits programmierte Webapplikation "tallo" wird ein Design benötigt. Tallo ähnelt den bereits bestehenden Zeiterfassungssystemen, soll sich aber anhand von Einfachheit, Speditivität und grafischer Eleganz von anderen abheben. Zudem sind Features geplant, die in anderen Systemen nicht oder nur mangelhaft implementiert sind.
Was benötigt wird:
1) Ein Log-In im Splashscreen-Style. Siehe Linkbox mit Beispiel. Das Login hebt sich vom Hauptdesign ab.
Elemente, die beim Login vorhanden sind: Email- und Passwortfeld, Passwort vergessen Link, Platz für das Logo des Accountinhabers (Firmenlogo o.ä).
Zum Logo des Accountinhabers: Wenn der Inhaber keines Hochgeladen hat soll das Login so angezeigt werden wie wenn kein Platz für ein Logo da wäre. Dies muss aber nicht separat nochmals als Design hochgeladen werden, es reicht mir eine Version mit einem Logo. Als Logo kann beispielsweise das Firmenlogo von ravelmark verwendet werden.
2) Das Hauptdesign, welches für die Webapplikation gilt. Also für alles andere ausser das Login. Hier ist beispielsweise die Navigation vorhanden und eine kleine Version vom tallo logo. In das Hauptdesign werden alle weiteren Inhalte der Applikation integriert (Projektliste, Zeiterfassung, Benutzer-Management, Statistiken, Abrechnungen, ...).
Für den Beispielinhalt hätte ich gern eine simple Liste/Tabelle, beispielsweise von Systembenutzern oder Projekten und kein Lorem Ipsum.
Für mich ist es relativ schwer, alles zu beschreiben, da ich von Anfang an bei tallo mitgearbeitet habe und dort mitten drin bin. Fragen sind also sehr willkommen und werden ausführlich beantwortet!

```html
<!DOCTYPE html>
<html lang="de">
<head>
<meta charset="utf-8">
<title>tallo – Login</title>
<link rel="stylesheet" href="https://fonts.googleapis.com/css2?family=Arimo:wght@400;700&display=swap">
<style>
  :root {
    --sky-light: #8fcdf5;
    --sky-mid: #3fa3ec;
    --sky-deep: #0987e6;
    --white: #ffffff;
    --panel-white: #ffffff;
    --tab-inactive: #eef4f9;
    --accent-blue: #1a8fe0;
    --label-grey: #444444;
    --field-bg: #f7f7f7;
    --field-border: #9a9a9a;
    --placeholder: #707070;
    --link-blue: #1a6fd6;
    --footer-top: #5e5e5e;
    --footer-bottom: #3a3a3a;
    --button-top: #f7c515;
    --button-bottom: #e09e00;
  }
  * { box-sizing: border-box; margin: 0; padding: 0; }
  html, body {
    width: 1200px;
    height: 900px;
    overflow: hidden;
  }
  body {
    font-family: "Arimo", Arial, sans-serif;
    background: radial-gradient(ellipse 560px 500px at 586px 360px,
      var(--sky-light) 0%, var(--sky-mid) 55%, var(--sky-deep) 100%);
    background-color: var(--sky-deep);
    position: relative;
  }
  .brand {
    position: absolute;
    left: 387px;
    top: 122px;
    color: var(--white);
  }
  .brand-name {
    display: block;
    font-size: 70px;
    font-weight: 400;
    line-height: 1;
    letter-spacing: -1px;
  }
  .brand-tagline {
    display: block;
    margin-top: 10px;
    font-size: 17px;
    font-weight: 400;
    letter-spacing: 0.2px;
  }
  .auth-tabs {
    position: absolute;
    left: 388px;
    top: 254px;
    display: flex;
    gap: 11px;
  }
  .auth-tab {
    height: 28px;
    padding: 0 17px;
    border-radius: 3px 3px 0 0;
    font-size: 15px;
    font-weight: 700;
    line-height: 29px;
    color: var(--accent-blue);
    background: var(--tab-inactive);
    letter-spacing: 0.4px;
  }
  .auth-tab.is-active { background: var(--panel-white); }
  .login-card {
    position: absolute;
    left: 388px;
    top: 282px;
    width: 397px;
    border-radius: 0 3px 3px 3px;
    overflow: hidden;
    box-shadow: 0 14px 14px -8px rgba(0, 40, 90, 0.45);
  }
  .login-body {
    background: var(--panel-white);
    height: 203px;
    padding: 31px 37px 0 37px;
  }
  .field-label {
    display: block;
    font-size: 14px;
    font-weight: 700;
    color: var(--label-grey);
    letter-spacing: 0.5px;
    margin-bottom: 6px;
  }
  .field-input {
    display: block;
    width: 322px;
    height: 27px;
    border: 2px solid var(--field-border);
    border-radius: 3px;
    background: var(--field-bg);
    box-shadow: inset 0 1px 2px rgba(0,0,0,0.15);
    font-family: inherit;
    font-size: 14px;
    color: var(--placeholder);
    padding: 0 9px;
    letter-spacing: 0.4px;
    margin-bottom: 21px;
  }
  .field-input::placeholder { color: var(--placeholder); }
  .field-input.is-password { letter-spacing: 5px; font-size: 16px; }
  .forgot-link {
    display: block;
    text-align: right;
    margin-top: -10px;
    padding-right: 8px;
    font-size: 13px;
    color: var(--link-blue);
    letter-spacing: 0.4px;
  }
  .login-footer {
    height: 75px;
    background: linear-gradient(var(--footer-top), var(--footer-bottom));
    position: relative;
  }
  .login-button {
    position: absolute;
    right: 38px;
    top: 19px;
    width: 99px;
    height: 37px;
    border: 1px solid #c98b00;
    border-radius: 4px;
    background: linear-gradient(var(--button-top), var(--button-bottom));
    color: var(--white);
    font-family: inherit;
    font-size: 21px;
    font-weight: 700;
    text-shadow: 0 1px 1px rgba(120, 70, 0, 0.6);
    cursor: pointer;
  }
</style>
</head>
<body>
  <header class="brand">
    <span class="brand-name">tallo</span>
    <span class="brand-tagline">pure time management</span>
  </header>

  <nav class="auth-tabs">
    <div class="auth-tab is-active">Login</div>
    <div class="auth-tab">Registrieren</div>
  </nav>

  <form class="login-card">
    <div class="login-body">
      <label class="field-label" for="email">Ihre E-Mail Adresse</label>
      <input class="field-input" id="email" type="text" placeholder="E-Mail@Beispiel.tld">
      <label class="field-label" for="password">Ihr Passwort</label>
      <input class="field-input is-password" id="password" type="password" value="passwort1">
      <a class="forgot-link" href="#">Passwort vergessen?</a>
    </div>
    <div class="login-footer">
      <button class="login-button" type="button">Login</button>
    </div>
  </form>
</body>
</html>
```